Small Group lesson study booklet

We need a design for a set of bible small group lesson studies. we would like to see a design that borrows from the Tessel logo. The age group we are aiming for is teens and young adults. We will need a sample cover and lesson page.

Scope: Five lessons in booklet form (one booklet covering them all.) We will also need a poster to go with the design of the booklet which we will pay for after the booklet design is done.

Attached is some sample work that has been done for the theme already.

When we pick a winner we will ask for the work to be completed with the rest of the lessons.

Target Market(s)

Teens and Young adults

Industry/Entity Type

Group

Font styles to use
Serif

Requirements
Must have
• - The concept has a food theme so anything along that line is fine.
• - Also clear transitions from section to section.
• - Racial diversity in the images.
• - A layout of a sample lesson and Cover. (Not the intro highlighted section in the sample lesson. it is only for context of the lesson.)
Should not have
• Crosses, doves and other generic christian symbols

```html
<!DOCTYPE html>
<html lang="en">
<head>
<meta charset="utf-8">
<title>Tessel – Small Group Lesson Study Cover</title>
<link rel="stylesheet" href="https://fonts.googleapis.com/css2?family=Roboto+Slab:wght@300&family=Poppins:wght@300;700&display=swap">
<style>
  :root {
    --page: #ffffff;
    --mint: #74c7ad;
    --mint-soft: #a3d9c6;
    --plum: #54444b;
    --plum-soft: #6e5d65;
    --icon-on-mint: #54444b;
    --icon-on-plum: #88c8b2;
  }
  * { margin: 0; padding: 0; box-sizing: border-box; }
  html, body {
    width: 1200px;
    height: 2187px;
    overflow: hidden;
    background: var(--page);
  }
  .cover {
    position: relative;
    width: 1200px;
    height: 2187px;
  }
  .band {
    position: absolute;
    left: 85px;
    width: 1023px;
  }
  .band--top { top: 70px; height: 1083px; background: var(--mint); }
  .band--bottom { top: 1153px; height: 966px; background: var(--plum); }

  .course {
    position: absolute;
    font-family: "Roboto Slab", Georgia, serif;
    font-weight: 300;
    line-height: 1;
    white-space: nowrap;
    color: var(--mint-soft);
  }
  .course--starter { left: 471px; top: 176px; font-size: 60px; }
  .course--salad   { left: 630px; top: 410px; font-size: 148px; }
  .course--entree  { left: 140px; top: 712px; font-size: 82px; }
  .course--dessert { left: 503px; top: 1440px; font-size: 90px; color: var(--plum-soft); }

  .title {
    position: absolute;
    left: 290px;
    top: 870px;
    width: 620px;
    text-align: center;
    color: var(--plum);
  }
  .title__name {
    display: flex;
    align-items: center;
    justify-content: center;
    gap: 26px;
    font-family: "Poppins", Arial, sans-serif;
    font-weight: 700;
    font-size: 132px;
    line-height: 1;
    letter-spacing: 2px;
  }
  .title__dot {
    width: 70px;
    height: 70px;
    border-radius: 50%;
    background: var(--plum);
  }
  .title__verse {
    margin-top: 18px;
    font-family: "Poppins", Arial, sans-serif;
    font-weight: 300;
    font-size: 44px;
    letter-spacing: 15px;
    line-height: 1;
  }

  .icons {
    position: absolute;
    inset: 0;
    width: 1200px;
    height: 2187px;
    fill: none;
    stroke-linecap: round;
    stroke-linejoin: round;
    stroke-width: 13;
  }
  .icons .on-mint { stroke: var(--icon-on-mint); }
  .icons .on-plum { stroke: var(--icon-on-plum); }
</style>
</head>
<body>
<main class="cover">
  <div class="band band--top"></div>
  <div class="band band--bottom"></div>

  <span class="course course--starter">starter</span>
  <span class="course course--salad">salad</span>
  <span class="course course--entree">entrée</span>
  <span class="course course--dessert">dessert</span>

  <div class="title">
    <div class="title__name"><span>Tessel</span><span class="title__dot"></span></div>
    <div class="title__verse">Ephesians 2:19</div>
  </div>

  <svg class="icons" viewBox="0 0 1200 2187" aria-hidden="true">
    <!-- drumstick -->
    <g class="on-mint">
      <path d="M330 320 H250 C205 320 188 290 190 258 C193 215 235 188 280 190 C325 192 352 212 360 232 L372 222 C366 205 380 190 396 196 C410 202 408 222 394 228 C404 240 392 256 378 248 L362 258 C370 290 360 320 330 320 Z"/>
      <path d="M262 290 C262 262 285 252 310 258"/>
    </g>
    <!-- soup bowl -->
    <g class="on-mint">
      <path d="M800 298 H945 C945 345 915 372 872 372 C830 372 800 345 800 298 Z"/>
      <path d="M845 375 H900"/>
      <path d="M900 290 L958 262"/>
      <path d="M843 272 C833 258 852 245 842 230"/>
      <path d="M872 272 C862 258 881 245 871 230"/>
      <path d="M901 272 C891 258 910 245 900 230"/>
    </g>
    <!-- apple -->
    <g class="on-mint">
      <path d="M545 565 C500 535 455 560 460 620 C465 680 505 712 545 700 C585 712 625 680 630 620 C635 560 590 535 545 565 Z"/>
      <path d="M545 565 V520"/>
      <path d="M552 540 C560 515 585 510 595 515 C590 540 570 548 552 540 Z"/>
    </g>
    <!-- bottle -->
    <g class="on-plum">
      <rect x="264" y="1308" width="62" height="22" rx="6"/>
      <path d="M270 1330 C258 1345 258 1360 258 1380 V1450 C258 1462 266 1466 276 1466 H314 C324 1466 332 1462 332 1450 V1380 C332 1360 332 1345 320 1330"/>
    </g>
    <!-- heart -->
    <g class="on-plum">
      <path d="M730 1392 L650 1312 C620 1282 640 1232 682 1234 C705 1235 720 1250 730 1266 C740 1250 755 1235 778 1234 C820 1232 840 1282 810 1312 Z"/>
    </g>
    <!-- bananas -->
    <g class="on-plum">
      <path d="M960 1500 C1010 1560 995 1650 915 1660 C875 1665 840 1640 828 1610 C860 1625 900 1622 930 1595 C955 1570 965 1535 960 1500 Z"/>
      <path d="M828 1568 C850 1600 910 1602 930 1582"/>
      <path d="M832 1535 C855 1565 905 1568 928 1552"/>
      <path d="M832 1535 C822 1548 822 1560 828 1568"/>
      <path d="M955 1500 L968 1490"/>
    </g>
    <!-- lemon -->
    <g class="on-plum">
      <path d="M455 1700 C445 1660 480 1630 525 1630 C560 1630 585 1648 595 1660"/>
      <path d="M455 1700 C450 1730 470 1758 510 1755 C530 1754 545 1750 560 1748"/>
      <circle cx="585" cy="1705" r="48"/>
      <circle cx="585" cy="1705" r="30"/>
      <path d="M585 1680 V1730 M560 1705 H610 M567 1687 L603 1723 M603 1687 L567 1723" stroke-width="5"/>
    </g>
    <!-- cutlery -->
    <g class="on-plum">
      <ellipse cx="190" cy="1870" rx="17" ry="22"/>
      <path d="M190 1892 V1988"/>
      <path d="M226 1852 V1890 C226 1900 234 1906 244 1906 C254 1906 262 1900 262 1890 V1852 M244 1852 V1888 M244 1906 V1988"/>
      <path d="M292 1850 C282 1870 280 1905 284 1925 H292 V1988"/>
    </g>
    <!-- carrot -->
    <g class="on-plum">
      <path d="M785 1995 C780 1988 782 1980 788 1972 L865 1900 C880 1888 905 1895 908 1915 C910 1928 905 1935 895 1945 L810 2000 C800 2005 790 2002 785 1995 Z"/>
      <path d="M895 1900 L905 1878 M905 1912 L925 1902 M900 1905 L920 1885"/>
    </g>
  </svg>
</main>
</body>
</html>
```